Flyer for Weightlifting Sports Club

We need a flyer to explain what weightlifting is and attract people of ages between 10 and 15 years old, so that they are encouraged to practice this sport with us. It should also serve to convince parents that it is a safe sport for children. We would like it to have an informal look, with the indispensable text and with many attractive graphics, even a comic type format. It could include the message that adults are also invited to try it. An invitation to try out for a week presenting the flyer should be visible.

Target Market(s)

Children from 10 to 15 years old

Font styles to use
Decorative
Script

Colors
b768aa
33a6d7
cadf82
f59296
f9ba93
faa54b

Requirements
Must have
• Information about our sport Drawings or pictures of child weightlifting

```html
<!DOCTYPE html>
<html lang="es">
<head>
<meta charset="utf-8">
<title>Club Deportivo Halterofilia Triana – Flyer</title>
<link href="https://fonts.googleapis.com/css2?family=Chelsea+Market&family=Oswald:wght@300;400;500&display=swap" rel="stylesheet">
<style>
  :root{
    --page:#e9e9ea;
    --purple:#3b0d3d;
    --purple-deep:#2a072c;
    --lime:#d4ea72;
    --lime-soft:#e6f29a;
    --orange:#f39a1e;
    --blue:#1a9fdc;
    --frame:#8a8a8a;
    --white:#ffffff;
    --text:#e8dfe9;
  }
  html,body{margin:0;padding:0;width:1141px;height:1200px;overflow:hidden;background:var(--page);}
  .flyer{position:absolute;left:148px;top:0;width:845px;height:1200px;background:linear-gradient(180deg,var(--purple) 0%,var(--purple-deep) 100%);overflow:hidden;font-family:'Oswald',sans-serif;color:var(--white);}
  .flyer-shapes{position:absolute;inset:0;}
  .club-mark{position:absolute;left:342px;top:392px;width:180px;height:180px;border-radius:50%;background:var(--white);display:flex;align-items:center;justify-content:center;text-align:center;font-family:'Chelsea Market',cursive;font-size:21px;line-height:1.15;color:var(--purple);}
  .title{position:absolute;left:0;width:845px;text-align:center;font-family:'Chelsea Market',cursive;font-weight:400;margin:0;line-height:1;}
  .title-club{top:612px;font-size:54px;color:var(--white);}
  .title-name{top:672px;font-size:54px;color:var(--orange);}
  .title-frame{position:absolute;left:35px;top:701px;width:762px;height:71px;border:1px solid var(--blue);border-top:none;}
  .title-frame::before,.title-frame::after{content:"";position:absolute;top:0;height:1px;background:var(--blue);width:36px;}
  .title-frame::before{left:0;} .title-frame::after{right:0;}
  .address{position:absolute;left:154px;top:743px;width:522px;height:47px;background:var(--blue);display:flex;align-items:center;justify-content:center;font-size:21px;font-weight:500;}
  .about{position:absolute;left:36px;top:818px;width:366px;font-size:13.4px;font-weight:300;line-height:17px;color:var(--text);}
  .about p{margin:0 0 17px;}
  .divider{position:absolute;left:422px;top:820px;width:1px;height:240px;background:rgba(255,255,255,.25);}
  .info{position:absolute;left:452px;top:820px;width:385px;}
  .info h2{font-family:'Chelsea Market',cursive;font-weight:400;font-size:26px;margin:0 0 8px;line-height:32px;}
  .fees{margin:0 0 10px;font-size:18px;font-weight:500;line-height:24px;}
  .hl{color:var(--orange);}
  .hours{margin:0;font-size:22px;font-weight:500;}
  .phone{position:absolute;left:440px;top:1030px;width:405px;height:60px;background:var(--blue);border-radius:30px 0 0 30px;}
  .phone-icon{position:absolute;left:8px;top:8px;width:44px;height:44px;border-radius:50%;background:var(--white);}
  .phone-label{position:absolute;left:72px;top:3px;font-size:14px;letter-spacing:.5px;line-height:18px;}
  .phone-number{position:absolute;left:70px;top:20px;font-family:'Chelsea Market',cursive;font-size:32px;line-height:36px;letter-spacing:1px;}
  .trial{position:absolute;left:110px;top:1152px;font-family:'Chelsea Market',cursive;font-size:20px;color:var(--white);margin:0;}
</style>
</head>
<body>
<main class="flyer">
  <svg class="flyer-shapes" width="845" height="1200" viewBox="0 0 845 1200">
    <defs>
      <linearGradient id="orangeFade" x1="0" y1="0" x2="0" y2="1">
        <stop offset="0" stop-color="#f6b21c"/><stop offset="1" stop-color="#ee7a12"/>
      </linearGradient>
      <linearGradient id="bottomOrange" x1="0" y1="0" x2="1" y2="1">
        <stop offset="0" stop-color="#e4500f"/><stop offset="1" stop-color="#f5a21c"/>
      </linearGradient>
      <linearGradient id="metal" x1="0" y1="0" x2="0" y2="1">
        <stop offset="0" stop-color="#f2f2f2"/><stop offset=".5" stop-color="#a9a9a9"/><stop offset="1" stop-color="#e0e0e0"/>
      </linearGradient>
      <linearGradient id="photoGym" x1="0" y1="0" x2="1" y2="1">
        <stop offset="0" stop-color="#2b2b2b"/><stop offset="1" stop-color="#5a5a55"/>
      </linearGradient>
      <linearGradient id="photoBoard" x1="0" y1="0" x2="0" y2="1">
        <stop offset="0" stop-color="#3f5e47"/><stop offset="1" stop-color="#34508a"/>
      </linearGradient>
      <linearGradient id="photoGirl" x1="0" y1="0" x2="1" y2="1">
        <stop offset="0" stop-color="#d9dde2"/><stop offset="1" stop-color="#b53d95"/>
      </linearGradient>
    </defs>
    <polygon points="0,0 175,0 0,175" fill="var(--lime-soft)"/>
    <polygon points="0,0 120,0 0,120" fill="var(--lime)"/>
    <polygon points="845,0 670,0 845,175" fill="var(--lime-soft)"/>
    <polygon points="845,0 730,0 845,115" fill="var(--lime)"/>
    <polygon points="0,450 130,580 0,580" fill="url(#orangeFade)"/>
    <polygon points="845,450 715,580 845,580" fill="url(#orangeFade)"/>
    <polygon role="img" aria-label="Foto: niño levantando una barra con discos en el gimnasio" points="182,74 407,314 147,554 0,407 0,260" fill="url(#photoGym)" stroke="var(--frame)" stroke-width="6"/>
    <polygon role="img" aria-label="Foto: niño disfrazado de superhéroe mostrando los brazos" points="185,59 432,289 672,54 432,-180" fill="url(#photoBoard)" stroke="var(--frame)" stroke-width="6"/>
    <polygon role="img" aria-label="Foto: niña levantando una mancuerna" points="687,69 845,227 845,400 687,554 447,314" fill="url(#photoGirl)" stroke="var(--frame)" stroke-width="6"/>
    <polygon points="0,1034 40,1060 85,1130 845,1130 845,1200 0,1200" fill="url(#bottomOrange)"/>
    <polygon points="650,1130 845,1130 845,1200 720,1200" fill="var(--lime)"/>
    <polygon points="82,1106 845,1106 845,1160 660,1160 620,1128 100,1128" fill="url(#metal)"/>
    <polygon points="100,1128 620,1128 660,1160 845,1160 845,1168 655,1168 615,1136 110,1136" fill="var(--purple)"/>
  </svg>

  <div class="club-mark">Halterofilia<br>Triana</div>

  <h1 class="title title-club">CLUB DEPORTIVO</h1>
  <div class="title-frame"></div>
  <h1 class="title title-name">HALTEROFILIA TRIANA</h1>
  <div class="address">C/. Jardín del Olivo, s/n. 41020-Ciudad</div>

  <div class="about">
    <p>La halterofilia o levantamiento de pesas es un deporte olímpico que se practica desde la antigüedad, y que llega a nuestros días como una actividad física que combina la fuerza, la velocidad, la agilidad y la técnica. Todo esto unido a la carga progresiva teniendo siempre en cuenta las posibilidades de cada persona, hace que sea muy beneficiosa su práctica a cualquier edad. En la infancia desarrolla la fuerza, corrige problemas posturales, estimula el crecimiento y mejora la coordinación y el rendimiento intelectual.</p>
    <p>En las personas adultas, además, favorece el aumento de la masa muscular, mejora el sistema cardiovascular, ayuda en la pérdida de grasa y aumenta la densidad ósea.</p>
    <p>Este deporte es muy inclusivo, ya que en las competiciones se tienen en cuenta el género, la edad y el peso corporal de los y las levantadoras.</p>
  </div>
  <div class="divider"></div>

  <section class="info">
    <h2>NUESTRAS CUOTAS:</h2>
    <p class="fees"><span class="hl">15€/mes</span> para menores de 18 años.<br><span class="hl">25€/mes</span> para mayores de 18 años.<br>Tres sesiones semanales de 60 minutos.</p>
    <h2>HORARIOS:</h2>
    <p class="hours">De lunes a viernes de <span class="hl">17:00 a 20:30</span></p>
  </section>

  <div class="phone">
    <div class="phone-icon">
      <svg width="44" height="44" viewBox="0 0 44 44" aria-hidden="true"><rect x="15" y="9" width="14" height="26" rx="2.5" fill="none" stroke="#333" stroke-width="2.4"/><circle cx="22" cy="31" r="1.5" fill="#333"/></svg>
    </div>
    <span class="phone-label">TELÉFONO DE CONTACTO</span>
    <span class="phone-number">XXXXXXXXX.</span>
  </div>

  <p class="trial">¡Presenta este flyer y prueba gratis una semana!</p>
</main>
</body>
</html>
```